Winery label for Birchfall Ridge Winery

New Winery on 265 acre farm in West Central Indiana, presently 10 acres of vineyard increasing to 16 acres in spring of 2018. An Estate Winery as wine will be produced from vine to bottle onsite. An event profit center is planned. Beautiful property with abundant wildlife including a large population of American Eagles , waterfowl, upland game, Marrow Fen Canal system traverses the property , abundant Native American artifacts on site , property bordered by Pell Run and its mouth at the Dunmoor River. Entered the Tolvane Open Vintners Trial in July 2016 as an amateur and won three medals for BRW Wine.
Updates
I am changing my BIRCHFALL RIDGE WINERY with the deer. It has a potential copywriter infringement. How can I send a jpeg pic to all designers ? .
Target Market(s)
100 mile radius, upscale easily recognized brand-label-logo, onsite sale, events,wine club distribution
Industry/Entity Type
Farm
Colors
Designer to choose colors to be used in the design.
Requirements
Must have
- eye appeal and brand recognition
Nice to have
- Read project description
Should not have
- Brand rights conflicts

```html
<!DOCTYPE html>
<html lang="en">
<head>
<meta charset="utf-8">
<title>Birchfall Ridge Winery – Label Design</title>
<link rel="stylesheet" href="https://fonts.googleapis.com/css2?family=Abril+Fatface&family=Playfair+Display:wght@700&family=Josefin+Sans:wght@600;700&display=swap">
<style>
  :root {
    --paper: #ffffff;
    --navy: #2a3048;
    --label-navy: #2c3249;
    --gold: #9a8358;
    --red: #c3262f;
    --display: "Abril Fatface", "Playfair Display", serif;
    --serif: "Playfair Display", Georgia, serif;
    --sans: "Josefin Sans", Arial, sans-serif;
  }
  html, body {
    margin: 0;
    padding: 0;
    width: 1193px;
    height: 1200px;
    overflow: hidden;
    background: var(--paper);
  }
  .canvas {
    position: relative;
    width: 1193px;
    height: 1200px;
  }
  .label { position: absolute; display: block; }
  .label--light { left: 262px; top: 33px; width: 658px; height: 406px; }
  .label--dark { left: 232px; top: 541px; width: 718px; height: 578px; }

  .wordmark { font-family: var(--display); font-size: 62px; text-anchor: middle; }
  .wordmark-sub { font-family: var(--serif); font-weight: 700; font-size: 18px; letter-spacing: 9px; text-anchor: middle; }
  .arc-caption { font-family: var(--serif); font-weight: 700; font-size: 15px; letter-spacing: 2.5px; }
  .badge-value { font-family: var(--sans); font-weight: 600; font-size: 22px; letter-spacing: 1px; text-anchor: middle; }
  .badge-caption { font-family: var(--sans); font-weight: 600; font-size: 9px; letter-spacing: 2px; }
  .varietal { font-family: var(--serif); font-weight: 700; font-size: 17px; letter-spacing: 2.5px; text-anchor: middle; }
  .spec { font-family: var(--sans); font-weight: 700; font-size: 18px; letter-spacing: 0.5px; }
  .spec-unit { font-size: 13px; letter-spacing: 1px; }

  .ink-navy { fill: var(--navy); }
  .ink-gold { fill: var(--gold); }
  .rule-navy { stroke: var(--navy); stroke-width: 1; fill: none; }
  .rule-gold { stroke: var(--gold); stroke-width: 1; fill: none; }
  .dotted { stroke-dasharray: 1 2; }
</style>
</head>
<body>
<main class="canvas">

  <!-- Brand lockup on white -->
  <svg class="label label--light" viewBox="0 0 658 406" aria-label="Birchfall Ridge Winery brand lockup">
    <g class="frame">
      <line class="rule-navy" x1="14" y1="43" x2="264" y2="43"/>
      <line class="rule-navy" x1="394" y1="43" x2="644" y2="43"/>
      <line class="rule-navy" x1="14" y1="400" x2="644" y2="400"/>
      <line class="rule-navy" x1="14" y1="43" x2="14" y2="400"/>
      <line class="rule-navy" x1="644" y1="43" x2="644" y2="400"/>
      <line class="rule-navy dotted" x1="1" y1="43" x2="1" y2="406"/>
      <line class="rule-navy dotted" x1="4.5" y1="43" x2="4.5" y2="406"/>
      <line class="rule-navy dotted" x1="8" y1="43" x2="8" y2="406"/>
      <line class="rule-navy dotted" x1="650" y1="43" x2="650" y2="406"/>
      <line class="rule-navy dotted" x1="653.5" y1="43" x2="653.5" y2="406"/>
      <line class="rule-navy dotted" x1="657" y1="43" x2="657" y2="406"/>
    </g>
    <circle class="brand-mark ink-navy" cx="329" cy="70" r="55"/>
    <text class="wordmark ink-navy" x="329" y="220">BIRCHFALL</text>
    <text class="wordmark ink-navy" x="329" y="283">RIDGE</text>
    <text class="wordmark-sub ink-navy" x="333" y="324">WINERY</text>
  </svg>

  <!-- Bottle label -->
  <svg class="label label--dark" viewBox="0 0 718 578" aria-label="Birchfall Ridge Winery cabernet sauvignon and syrah bottle label">
    <defs>
      <path id="arc-estate" d="M 219 66 A 320 320 0 0 1 499 66"/>
      <path id="arc-barrel" d="M 97 440 A 32 32 0 0 1 161 440"/>
      <path id="arc-aged" d="M 99 459 A 32 32 0 0 0 159 459"/>
      <path id="arc-estate-badge" d="M 557 440 A 32 32 0 0 1 621 440"/>
      <path id="arc-winery-badge" d="M 559 459 A 32 32 0 0 0 619 459"/>
    </defs>
    <rect class="label-ground" width="718" height="578" fill="var(--label-navy)"/>

    <g class="frame">
      <line class="rule-gold" x1="53" y1="44" x2="200" y2="44"/>
      <line class="rule-gold" x1="518" y1="44" x2="665" y2="44"/>
      <line class="rule-gold" x1="53" y1="526" x2="172" y2="526"/>
      <line class="rule-gold" x1="546" y1="526" x2="665" y2="526"/>
      <line class="rule-gold dotted" x1="44" y1="44" x2="44" y2="526"/>
      <line class="rule-gold dotted" x1="48" y1="44" x2="48" y2="526"/>
      <line class="rule-gold" x1="53" y1="44" x2="53" y2="526"/>
      <line class="rule-gold" x1="665" y1="44" x2="665" y2="526"/>
      <line class="rule-gold dotted" x1="670" y1="44" x2="670" y2="526"/>
      <line class="rule-gold dotted" x1="674" y1="44" x2="674" y2="526"/>
    </g>

    <text class="arc-caption ink-gold"><textPath href="#arc-estate" startOffset="50%" text-anchor="middle">WINERY ESTATE</textPath></text>

    <circle class="brand-mark" cx="359" cy="137" r="45" fill="var(--red)"/>

    <text class="wordmark ink-gold" x="359" y="294">BIRCHFALL</text>
    <text class="wordmark ink-gold" x="359" y="357">RIDGE</text>
    <text class="wordmark-sub ink-gold" x="363" y="398">WINERY</text>

    <g class="badge badge--vintage">
      <text class="badge-caption ink-gold"><textPath href="#arc-barrel" startOffset="50%" text-anchor="middle">BARREL</textPath></text>
      <text class="badge-value ink-gold" x="129" y="458">( 2015 )</text>
      <text class="badge-caption ink-gold"><textPath href="#arc-aged" startOffset="50%" text-anchor="middle">AGED</textPath></text>
    </g>

    <g class="badge badge--estate">
      <text class="badge-caption ink-gold"><textPath href="#arc-estate-badge" startOffset="50%" text-anchor="middle">ESTATE</textPath></text>
      <text class="badge-value ink-gold" x="589" y="458">( BRW )</text>
      <text class="badge-caption ink-gold"><textPath href="#arc-winery-badge" startOffset="50%" text-anchor="middle">WINERY</textPath></text>
    </g>

    <text class="varietal ink-gold" x="359" y="509">CABERNET</text>
    <text class="varietal ink-gold" x="359" y="533">SAUVIGNON &amp; SYRAH</text>

    <text class="spec ink-gold" x="26" y="554">13.5 <tspan class="spec-unit">ALC/VOL</tspan></text>
    <text class="spec ink-gold" x="692" y="554" text-anchor="end">750 <tspan class="spec-unit">ML</tspan></text>
  </svg>

</main>
</body>
</html>
```